43 Year Old Construction firm needs Updated Business Card & Stationery Design

We are an established and well known (in our market) commercial construction firm. We need a cleaner and more modern look for our corporate identity material. We would like to continue to use our current colors and logo.
We are thinking about incorporating a slogan on our business card (either front or back): "Striving to be the most trusted builder in our market." The text could change at some point. Our website is www.kvoplarn.com . Sample card is attached. Some will have more phone numbers, etc...
Updates

Target Market(s)

Commercial and institutional clients.

Industry/Entity Type

Construction Company

Contact Information for Business Card

See attached for existing card. But don't be constrained.

Requirements
Must have
• Logo, name, title, address, website, email, phone numbers (as few as one, as many as three)
• Slogan on front or back "Striving to be the most trusted builder in our market"
• Use existing logo and colors

```html
<!DOCTYPE html>
<html lang="en">
<head>
<meta charset="utf-8">
<title>Kvoplarn Constructors – Business Card</title>
<link rel="stylesheet" href="https://fonts.googleapis.com/css2?family=Cormorant+SC:wght@600&family=Crimson+Pro:wght@400;600&display=swap">
<style>
  :root {
    --navy: #0f3c7a;
    --navy-deep: #0a2c5e;
    --navy-light: #1d5aa3;
    --green: #1f9a4a;
    --ink: #4a4a4a;
    --paper: #ffffff;
    --stage: #e6e8eb;
    --slogan: #dfe7f2;
  }
  * { box-sizing: border-box; margin: 0; padding: 0; }
  html, body { width: 1200px; height: 871px; overflow: hidden; }
  body {
    background: var(--stage);
    font-family: "Crimson Pro", Georgia, serif;
    position: relative;
  }
  .card {
    position: absolute;
    top: 287px;
    width: 520px;
    height: 297px;
    overflow: hidden;
    box-shadow: 0 6px 18px rgba(0,0,0,.18);
  }

  /* Back */
  .card-back {
    left: 60px;
    background: linear-gradient(135deg, var(--navy-light) 0%, var(--navy) 45%, var(--navy-deep) 100%);
    display: flex;
    flex-direction: column;
    align-items: center;
    justify-content: center;
    gap: 18px;
  }
  .card-back .wordmark {
    color: #ffffff;
    font-weight: 600;
    font-size: 34px;
    line-height: 1.1;
    letter-spacing: 2px;
    text-transform: uppercase;
    text-align: center;
  }
  .card-back .slogan {
    color: var(--slogan);
    font-size: 16px;
    letter-spacing: .3px;
    text-align: center;
    max-width: 420px;
  }

  /* Front */
  .card-front { left: 620px; background: var(--paper); }
  .card-front .wordmark {
    position: absolute;
    left: 26px;
    top: 86px;
    width: 240px;
    display: flex;
    align-items: center;
    gap: 10px;
    color: var(--navy);
    font-weight: 600;
    font-size: 22px;
    line-height: 1.1;
    letter-spacing: 1px;
    text-transform: uppercase;
  }
  .wordmark .mark-square {
    width: 16px; height: 16px; background: var(--navy); flex: none;
  }
  .contact {
    position: absolute;
    left: 292px;
    top: 46px;
    width: 200px;
    color: var(--ink);
  }
  .contact .person-name {
    font-family: "Cormorant SC", Georgia, serif;
    font-weight: 600;
    font-size: 22px;
    color: var(--navy);
    line-height: 1;
    letter-spacing: .5px;
  }
  .contact .person-title {
    font-family: "Cormorant SC", Georgia, serif;
    font-weight: 600;
    font-size: 16px;
    color: var(--green);
    line-height: 1.2;
    letter-spacing: .5px;
  }
  .contact .rule {
    border-top: 2px dotted var(--navy);
    margin: 5px 0;
  }
  .contact .address { font-size: 14px; line-height: 1.15; }
  .contact ul { list-style: none; font-size: 14px; line-height: 1.25; }
  .contact li { display: flex; align-items: center; gap: 7px; }
  .contact li svg { width: 11px; height: 11px; fill: var(--navy); flex: none; }

  .band {
    position: absolute;
    left: 0; right: 0; bottom: 0;
    height: 66px;
  }
  .band .band-line { height: 3px; background: var(--navy); margin-bottom: 3px; }
  .band .band-stripe { height: 5px; background: var(--green); }
  .band .band-block {
    height: 46px;
    margin-top: 3px;
    background: linear-gradient(90deg, var(--navy-light), var(--navy) 50%, var(--navy-deep));
  }
  .band .band-foot { height: 3px; background: var(--green); }
  .band .band-edge { height: 3px; background: var(--navy); }
</style>
</head>
<body>
  <section class="card card-back" aria-label="Card back">
    <span class="wordmark">Kvoplarn<br>Constructors</span>
    <p class="slogan">Striving to be the most trusted builder in our market.</p>
  </section>

  <section class="card card-front" aria-label="Card front">
    <div class="wordmark"><span class="mark-square"></span><span>Kvoplarn<br>Constructors</span></div>

    <div class="contact">
      <p class="person-name">Dale Morrow</p>
      <p class="person-title">CEO/Founder</p>
      <div class="rule"></div>
      <p class="address">4120 harbor lane<br>riverton, MO 63001</p>
      <div class="rule"></div>
      <ul>
        <li><svg viewBox="0 0 24 24"><path d="M6.6 10.8a15.1 15.1 0 0 0 6.6 6.6l2.2-2.2a1 1 0 0 1 1-.25 11.4 11.4 0 0 0 3.6.57 1 1 0 0 1 1 1V20a1 1 0 0 1-1 1A17 17 0 0 1 3 4a1 1 0 0 1 1-1h3.5a1 1 0 0 1 1 1 11.4 11.4 0 0 0 .57 3.6 1 1 0 0 1-.25 1z"/></svg>555.014.2290</li>
        <li><svg viewBox="0 0 24 24"><path d="M2 5h20v14H2zm2 2v.5l8 5 8-5V7zm0 3v7h16v-7l-8 5z"/></svg>dale@kvoplarn.com</li>
        <li><svg viewBox="0 0 24 24"><circle cx="12" cy="12" r="10"/></svg>www.kvoplarn.com</li>
      </ul>
    </div>

    <div class="band">
      <div class="band-line"></div>
      <div class="band-stripe"></div>
      <div class="band-block"></div>
      <div class="band-foot"></div>
      <div class="band-edge"></div>
    </div>
  </section>
</body>
</html>
```